Classic/Royal 5 Items Black coloured Stationery Design

Hello,
I'm looking for an Elegant Stationery set consists of 5 items as the following,
1- Letterhead
2- Business Card
3- Invoice
4- CD/DVD with their Envelope Design
5- Envelope
To let the project move ahead easily, I've included a folder consists many designs I liked from various design sites and it consists of,
1- Business card
2- Corporate Identity
3- Invoice
4- Miscellanies
Inside the first three folders, you will find a folder named "Recommended", it contains designs that I like so much and hoping to have a design like them.
The "Miscellanies" folder got some designs for Inspiration.
I'm waiting for some greats designs, a joomla template designer is a bonus for me as I will need him to design the website layer soon.
Due to upload problems at ArtHerdly, I've uploaded the folder in a .rar archive at multiple site and here is the link http://zup.qx/TRALVBNE .
Thank you
Update :- You can use this alternative download link from my Google drive to download the designs
https://files.plomwex.net/file/d/7Kq2ZpR4m8sVxT1nLw9cYb3HfJd5

```html
<!DOCTYPE html>
<html lang="en">
<head>
<meta charset="utf-8">
<title>Vale Crest – Business Card</title>
<link rel="stylesheet" href="https://fonts.googleapis.com/css2?family=Cinzel:wght@600;700&family=Oswald:wght@400&family=Questrial&display=swap">
<style>
  :root {
    --page: #ffffff;
    --card: #000000;
    --blue-light: #3d73bd;
    --blue-deep: #1a5fb0;
    --blue-accent: #3a6cb5;
    --silver: #a9abae;
    --white: #ffffff;
  }
  * { margin: 0; padding: 0; box-sizing: border-box; }
  html, body { width: 891px; height: 1200px; overflow: hidden; background: var(--page); }
  .sheet { position: relative; width: 891px; height: 1200px; }
  .card {
    position: absolute; left: 0; width: 891px; height: 557px; overflow: hidden;
  }
  .card--front { top: 17px; }
  .card--back { top: 621px; }
  .card__bg { position: absolute; inset: 0; width: 100%; height: 100%; }
  .brand { position: absolute; text-align: center; transform: translateX(-50%); white-space: nowrap; }
  .brand__name {
    font-family: "Cinzel", serif; font-weight: 600; color: var(--silver);
    font-size: 40px; line-height: 1; letter-spacing: 1px;
  }
  .brand__tagline {
    font-family: "Questrial", sans-serif; color: var(--silver);
    font-size: 17px; margin-top: 10px;
  }
  .card--front .brand { left: 457px; top: 284px; }
  .card--back .brand { left: 761px; top: 120px; }
  .person { position: absolute; left: 70px; top: 182px; text-align: center; width: 258px; }
  .person__name {
    font-family: "Cinzel", serif; font-weight: 700; font-size: 36px; color: var(--white);
    line-height: 1;
  }
  .person__name .surname { color: var(--blue-accent); }
  .person__role {
    font-family: "Cinzel", serif; font-weight: 700; font-size: 20px; color: var(--white);
    margin-top: 6px; white-space: nowrap;
  }
  .contact { position: absolute; display: flex; align-items: center; gap: 11px; }
  .contact__key {
    width: 36px; height: 36px; background: var(--blue-accent); color: var(--white);
    font-family: "Questrial", sans-serif; font-weight: 700; font-size: 21px;
    display: flex; align-items: center; justify-content: center;
  }
  .contact__value {
    font-family: "Oswald", sans-serif; font-size: 19px; color: var(--white);
    letter-spacing: 2px; white-space: nowrap;
  }
  .contact--address { left: 77px; top: 326px; }
  .contact--mobile { left: 77px; top: 391px; }
  .contact--fax { left: 311px; top: 391px; }
  .contact--email { left: 77px; top: 452px; }
  .contact--web { left: 311px; top: 450px; }
</style>
</head>
<body>
<div class="sheet">
  <section class="card card--front">
    <svg class="card__bg" viewBox="0 0 1039 650" preserveAspectRatio="none" aria-hidden="true">
      <rect width="1039" height="650" fill="var(--blue-light)"/>
      <path d="M168,0 H1039 V440 C990,580 910,650 822,650 H0 V205 C40,100 95,15 168,0 Z" fill="var(--blue-deep)"/>
      <path d="M185,0 H1039 V458 C990,575 920,645 840,650 H0 V222 C40,110 100,18 185,0 Z" fill="var(--card)"/>
    </svg>
    <div class="brand">
      <div class="brand__name">Vale Crest</div>
      <div class="brand__tagline">Hotels and General Supplies</div>
    </div>
  </section>

  <section class="card card--back">
    <svg class="card__bg" viewBox="0 0 1039 650" preserveAspectRatio="none" aria-hidden="true">
      <rect width="1039" height="650" fill="var(--blue-light)"/>
      <path d="M168,0 H1039 V440 C990,580 910,650 822,650 H0 V205 C40,100 95,15 168,0 Z" fill="var(--blue-deep)"/>
      <path d="M185,0 H1039 V458 C990,575 920,645 840,650 H0 V222 C40,110 100,18 185,0 Z" fill="var(--card)"/>
    </svg>
    <div class="brand">
      <div class="brand__name">Vale Crest</div>
      <div class="brand__tagline">Hotels and General Supplies</div>
    </div>
    <div class="person">
      <div class="person__name">JANE <span class="surname">ROE</span></div>
      <div class="person__role">MANAGING DIRECTOR</div>
    </div>
    <div class="contact contact--address"><span class="contact__key">A</span><span class="contact__value">67890 Birchfield Lane Arlington 22201</span></div>
    <div class="contact contact--mobile"><span class="contact__key">M</span><span class="contact__value">5550192834</span></div>
    <div class="contact contact--fax"><span class="contact__key">F</span><span class="contact__value">5550192834</span></div>
    <div class="contact contact--email"><span class="contact__key">E</span><span class="contact__value">hello@valecrest.com</span></div>
    <div class="contact contact--web"><span class="contact__key">W</span><span class="contact__value">www.valecrest.com</span></div>
  </section>
</div>
</body>
</html>
```